Design a Corporate Cover Page

All of our company reports have a fancy cover page and it's time to update it with something new and fresh. We're looking for a cover page design in Microsoft word (the graphics can be done in any program). I've attached our previous design, vectors of our logos in a variety of colors and our corporate colors. Requirements:

- Must be in Microsoft word
- Must have areas in which we can put the proposal name, information and the senders contact information. See the attached document for an example

In a nutshell we are a consulting company for the construction industry. We help major project stay on time and in budget. You can learn more about our company and www.advisorynimbex.com. Our beta website (for the latest and greatest info) is at: http://v2.advisorynimbex.com/

Edit 12:02PM : We would like our office locations to be noted on the cover page. They are: Washington DC (Headquarters), Los Angeles, Dallas and Philadelphia.

```html
<!DOCTYPE html>
<html lang="en">
<head>
<meta charset="utf-8">
<title>Proposal Cover – Nimbex Project Controls</title>
<link href="https://fonts.googleapis.com/css2?family=Montserrat:wght@300;400;600;700&display=swap" rel="stylesheet">
<style>
  :root {
    --backdrop: #e4e4e4;
    --cover-black: #1b1b1b;
    --ink-white: #ffffff;
    --ink-soft: #d6d6d6;
    --ink-muted: #a9a9a9;
    --brand-navy: #1d2f6b;
    --photo-light: #dcd9d4;
    --photo-mid: #7a6650;
    --photo-dark: #2a2622;
  }
  * { margin: 0; padding: 0; box-sizing: border-box; }
  html, body {
    width: 1200px; height: 800px; overflow: hidden;
    background: var(--backdrop);
    font-family: "Montserrat", Arial, sans-serif;
  }
  .canvas { position: relative; width: 1200px; height: 800px; }
  .cover {
    position: absolute; left: 341px; top: 32px;
    width: 518px; height: 736px;
    background: var(--cover-black);
    overflow: hidden;
    box-shadow: 0 2px 8px rgba(0,0,0,.25);
  }
  .cover-art { position: absolute; inset: 0; width: 518px; height: 736px; }
  .brand-tab {
    position: absolute; left: 44px; top: 0;
    width: 114px; height: 80px;
    background: var(--ink-white);
    border-radius: 0 0 14px 14px;
    display: flex; align-items: center; justify-content: center;
  }
  .brand-name {
    color: var(--brand-navy);
    font-weight: 700; font-size: 21px; letter-spacing: 1px;
  }
  .proposal-block { position: absolute; left: 37px; top: 150px; color: var(--ink-white); }
  .proposal-label { font-weight: 700; font-size: 21px; letter-spacing: .3px; line-height: 26px; }
  .proposal-title { font-weight: 400; font-size: 15px; line-height: 19px; letter-spacing: 0; }
  .proposal-subtitle {
    margin-top: 8px; font-weight: 400; font-size: 9.5px; line-height: 13px;
    letter-spacing: .2px; color: var(--ink-soft);
  }
  .marker {
    position: absolute; left: 0; top: 331px; width: 0; height: 0;
    border-top: 11px solid transparent; border-bottom: 11px solid transparent;
    border-left: 12px solid var(--ink-white);
  }
  .years {
    position: absolute; left: 37px; top: 316px;
    color: var(--ink-white); font-weight: 700; font-size: 36px; line-height: 40px;
  }
  .contact-col {
    position: absolute; top: 672px;
    color: var(--ink-muted); font-size: 7px; line-height: 10px; letter-spacing: .2px;
    text-transform: uppercase; white-space: nowrap;
  }
  .contact-person { left: 81px; }
  .contact-address { left: 180px; }
  .contact-company { left: 340px; }
</style>
</head>
<body>
<div class="canvas">
  <section class="cover">
    <svg class="cover-art" viewBox="0 0 518 736" role="img" aria-label="Photograph of glass high-rise towers against a pale sky">
      <defs>
        <linearGradient id="photoTone" x1="1" y1="0" x2="0" y2="1">
          <stop offset="0" stop-color="#dcd9d4"/>
          <stop offset="0.45" stop-color="#7a6650"/>
          <stop offset="1" stop-color="#2a2622"/>
        </linearGradient>
      </defs>
      <polygon points="518,10 0,530 0,736 518,736" fill="url(#photoTone)"/>
      <polygon points="262,470 8,728 514,722" fill="#1b1b1b"/>
      <line x1="518" y1="10" x2="0" y2="530" stroke="#ffffff" stroke-width="1.5"/>
      <polygon points="262,470 8,728 514,722" fill="none" stroke="#ffffff" stroke-width="2"/>
    </svg>

    <div class="brand-tab"><span class="brand-name">NIMBEX</span></div>

    <div class="proposal-block">
      <p class="proposal-label">PROPOSAL</p>
      <p class="proposal-title">THE NEW HARWELL HOSPITAL</p>
      <p class="proposal-title">WASHINGTON, DC</p>
      <p class="proposal-subtitle">REQUEST FOR PROPOSAL RESPONSE<br>CRITICAL PATH METHOD SCHEDULING</p>
    </div>

    <span class="marker"></span>
    <p class="years">2018<br>2019</p>

    <p class="contact-col contact-person">Point of contact<br>Daniel Marsh<br>President</p>
    <p class="contact-col contact-address">dmarsh@advisorynimbex.com<br>2240 Linden Avenue, Suite 410<br>Silver Spring, MD 20910</p>
    <p class="contact-col contact-company">Nimbex Project Controls<br>240.555.0187</p>
  </section>
</div>
</body>
</html>
```